Podcast cover art (not a logo)

I’m launching an audio-only podcast for parents of neurodivergent children. The podcast is meant to feel like a calm, trusted professional voice — not a brand or a performance.

Style direction:
--Clean and minimal
--Calm and grounded
--Professional, not playful
--Nothing flashy, loud, or busy
--No cartoon imagery

Content on the cover:
--Podcast title: Rooted in Listening
--Subtitle or tagline: Supporting Neurodivergent Kids with Science, Not Shame (or Understanding Neurodivergent Kids)
--No episode numbers, no dates

Design preferences:
--Text-forward design
--Neutral or soft colors (muted blues, grays, off-whites)
--High contrast for readability at small sizes
--Simple, timeless font

What I do NOT want:
--A logo or branding system
--Illustrations of children or families
--Bright colors or playful graphics
--Trendy fonts or visual effects

Technical requirements:
--Square image
--3000 × 3000 pixels
--RGB color mode
--JPEG or PNG
--File size under 500 KB

Deliverables:
--Final cover art file
--Optional: one or two alternate background color versions

```html
<!DOCTYPE html>
<html lang="en">
<head>
<meta charset="utf-8">
<title>Rooted in Listening — Cover Variations</title>
<link rel="stylesheet" href="https://fonts.googleapis.com/css2?family=Bebas+Neue&family=Oswald:wght@500&family=Outfit:wght@200;300;500;600&family=Poppins:ital,wght@0,400;0,800;1,400&display=swap">
<style>
  :root {
    --board: #4f4f4f;
    --navy: #1e2f4e;
    --navy-soft: #3a4b6e;
    --slate: #333f55;
    --deep-blue: #1f3b66;
    --sky: #c3d6f3;
    --cream: #fdfdf4;
    --cream-shade: #dfe2e6;
    --lavender: #dfdff5;
    --lavender-top: #dfddf5;
    --mist: #e6ebf8;
    --pale-text: #e0e0f5;
  }
  * { margin: 0; padding: 0; box-sizing: border-box; }
  html, body {
    width: 1200px;
    height: 1195px;
    overflow: hidden;
    background: var(--board);
  }
  .board {
    position: relative;
    width: 1200px;
    height: 1195px;
  }
  .cover {
    position: absolute;
    width: 532px;
    height: 532px;
    display: block;
    box-shadow: 0 10px 18px rgba(0,0,0,0.28);
  }
  .cover--sky      { left: 52px;  top: 54px;  }
  .cover--path     { left: 616px; top: 52px;  }
  .cover--stacked  { left: 52px;  top: 612px; }
  .cover--light    { left: 617px; top: 612px; }
</style>
</head>
<body>
<main class="board">

  <!-- Variation 1: condensed stacked title on sky blue -->
  <svg class="cover cover--sky" viewBox="0 0 590 590" aria-label="Rooted in Listening cover, sky blue">
    <rect width="590" height="590" fill="var(--sky)"/>
    <text x="115" y="212" font-family="'Bebas Neue', sans-serif" font-size="148" fill="var(--navy)" textLength="356" lengthAdjust="spacingAndGlyphs">ROOTED</text>
    <text transform="translate(164 306) rotate(-90)" font-family="'Bebas Neue', sans-serif" font-size="52" fill="var(--navy)" textLength="78" lengthAdjust="spacingAndGlyphs">IN</text>
    <text x="174" y="306" font-family="'Bebas Neue', sans-serif" font-size="116" fill="var(--navy)" textLength="298" lengthAdjust="spacingAndGlyphs">LISTENING</text>
    <circle cx="137" cy="430" r="26" fill="var(--navy)"/>
    <text font-family="'Outfit', sans-serif" font-weight="500" font-size="19" fill="var(--navy)" letter-spacing="-0.3">
      <tspan x="176" y="426">Supporting Neurodivergent</tspan>
      <tspan x="176" y="448">Kids with Science, Not Shame</tspan>
    </text>
  </svg>

  <!-- Variation 2: title over soft artwork area on cream -->
  <svg class="cover cover--path" viewBox="0 0 590 590" aria-label="Rooted in Listening cover, cream">
    <defs>
      <linearGradient id="artwork-tone" x1="0" y1="1" x2="1" y2="0">
        <stop offset="0" stop-color="var(--cream-shade)"/>
        <stop offset="0.5" stop-color="var(--cream)"/>
        <stop offset="1" stop-color="var(--cream-shade)"/>
      </linearGradient>
    </defs>
    <rect width="590" height="590" fill="var(--cream)"/>
    <rect class="artwork-area" width="590" height="590" fill="url(#artwork-tone)" role="img" aria-label="Space for a winding road illustration crossing the cover"/>
    <text x="71" y="120" font-family="'Outfit', sans-serif" font-weight="600" font-size="56" fill="var(--navy-soft)" letter-spacing="-1">Rooted</text>
    <text x="230" y="262" font-family="'Outfit', sans-serif" font-weight="600" font-size="50" fill="var(--navy)" letter-spacing="-1">in</text>
    <text x="556" y="398" text-anchor="end" font-family="'Outfit', sans-serif" font-weight="600" font-size="54" fill="var(--navy-soft)" letter-spacing="-1">Listening</text>
    <text font-family="'Oswald', sans-serif" font-weight="500" font-size="19" fill="var(--navy)">
      <tspan x="41" y="512">U<tspan font-size="15">NDERSTANDING</tspan></tspan>
      <tspan x="41" y="538">N<tspan font-size="15">EURODIVERGENT</tspan> K<tspan font-size="15">IDS</tspan></tspan>
    </text>
  </svg>

  <!-- Variation 3: stacked rounded labels on lavender -->
  <svg class="cover cover--stacked" viewBox="0 0 590 590" aria-label="Rooted in Listening cover, stacked labels">
    <rect width="590" height="590" fill="var(--lavender)"/>
    <g transform="rotate(-3 292 150)">
      <rect x="154" y="96" width="278" height="114" rx="34" fill="var(--slate)"/>
      <text x="293" y="172" text-anchor="middle" font-family="'Poppins', sans-serif" font-weight="800" font-size="54" fill="var(--pale-text)" letter-spacing="-1">Rooted</text>
    </g>
    <g transform="rotate(3 304 262)">
      <rect x="234" y="212" width="142" height="104" rx="28" fill="var(--deep-blue)"/>
      <text x="305" y="284" text-anchor="middle" font-family="'Poppins', sans-serif" font-weight="800" font-size="56" fill="var(--pale-text)" letter-spacing="-1">in</text>
    </g>
    <rect x="140" y="322" width="310" height="106" rx="32" fill="var(--navy)"/>
    <text x="295" y="394" text-anchor="middle" font-family="'Poppins', sans-serif" font-weight="800" font-size="50" fill="var(--pale-text)" letter-spacing="-1">Listening</text>
    <text text-anchor="middle" font-family="'Poppins', sans-serif" font-style="italic" font-size="22" fill="var(--navy)">
      <tspan x="295" y="474">Understanding</tspan>
      <tspan x="295" y="503">Neurodivergent Kids</tspan>
    </text>
  </svg>

  <!-- Variation 4: light type with soft curved band -->
  <svg class="cover cover--light" viewBox="0 0 590 590" aria-label="Rooted in Listening cover, light type">
    <rect width="590" height="590" fill="var(--lavender-top)"/>
    <path d="M 0 334 Q 295 410 590 334 L 590 590 L 0 590 Z" fill="var(--mist)"/>
    <text text-anchor="middle" font-family="'Outfit', sans-serif" font-weight="200" font-size="82" fill="var(--navy)" letter-spacing="-3">
      <tspan x="296" y="176">Rooted</tspan>
      <tspan x="296" y="258">in Listening</tspan>
    </text>
    <text text-anchor="middle" font-family="'Poppins', sans-serif" font-size="17" fill="var(--navy)" letter-spacing="3.2">
      <tspan x="296" y="466">Supporting Neurodivergent</tspan>
      <tspan x="296" y="489">Kids with Science.</tspan>
      <tspan x="296" y="512">Not Shame</tspan>
    </text>
  </svg>

</main>
</body>
</html>
```